New Electrical Contractor looking for local work

I have just started working for myself as an Electrical Contractor, based in the eastern suburbs of Melbourne. I want to advertise in the local area so hopefully I can create a client base that is close to home, so I thought a flyer that I could drop in letterboxes could be a good start. Most of my experience has been domestic houses, so ideally this is the work I would like to get more of.

Here is a list of the work I usually do:
Extensions / Renovations
Safety Switch and Switchboard Upgrades
LED Lighting including downlights/light fittings and LED strip light
Re-wires
Maintenance

I have also added a couple of images of LED strip lights and how they can be used in homes. There are a lot more on google images if anyone thinks they could be of use.

These are my details:
Business name - Dale Hurst Electrical
Phone - 0437 216 580
ABN - 42 318 570 264
REC - 38517
Email - hurstelectrical@sparkmailbox.net

I will attach my business logo and business card
Updates

Could I please ask for all designs to delete the "(contractors registration number)" text.

Only REC 38517 needs to be displayed.

Thank you kindly

Industry/Entity Type

Business

Requirements
Must have
• My contact details, ie. Name, Phone, email, ABN, REC etc

```html
<!DOCTYPE html>
<html lang="en">
<head>
<meta charset="utf-8">
<title>Dale Hurst Electrical</title>
<link rel="stylesheet" href="https://fonts.googleapis.com/css2?family=Arimo:wght@400;700&family=Archivo+Black&family=Cabin:wght@700&display=swap">
<style>
  :root {
    --brand-red: #b91a10;
    --white: #ffffff;
    --contact-red: #e8170d;
    --brick-light: #d8bdb5;
    --brick-mid: #c8a59c;
    --brick-dark: #b38f86;
  }
  * { margin: 0; padding: 0; box-sizing: border-box; }
  html, body { width: 938px; height: 1200px; overflow: hidden; background: var(--white); }
  .flyer { position: relative; width: 938px; height: 1200px; font-family: "Arimo", Arial, sans-serif; }
  .wall {
    position: absolute; left: 0; top: 0; width: 938px; height: 1058px;
    background: linear-gradient(160deg, var(--brick-light), var(--brick-mid) 50%, var(--brick-dark));
  }
  .fixture { position: absolute; border-radius: 4px; }
  .fixture--track { left: 0; top: 0; width: 212px; height: 100px; background: linear-gradient(#c9c3bf, #a9a29e); }
  .fixture--flood { left: 18px; top: 155px; width: 170px; height: 75px; background: linear-gradient(#eceaea, #b5b2b0); border-radius: 30px; }
  .fixture--sconce { left: 38px; top: 295px; width: 165px; height: 160px; background: linear-gradient(#d0c9c2, #f1ece4); }
  .fixture--lamp { left: 55px; top: 520px; width: 135px; height: 197px; background: linear-gradient(#f1e4cc, #8a6a4b); }
  .fixture--lantern { left: 18px; top: 798px; width: 152px; height: 205px; background: linear-gradient(#3e5448, #263a30); border-radius: 10px; }
  .fixture--chandelier { left: 780px; top: 0; width: 140px; height: 262px; background: linear-gradient(#e7d9a8, #c9ab5e); border-radius: 50% 50% 40% 40%; }
  .fixture--fan { left: 736px; top: 295px; width: 172px; height: 120px; background: linear-gradient(90deg, #7b3a36, #bdbdc0 50%, #7b3a36); border-radius: 40px; }
  .fixture--board { left: 760px; top: 530px; width: 140px; height: 255px; background: linear-gradient(#d3d4d2, #9a9c9a); border-radius: 2px; }
  .fixture--outlet { left: 790px; top: 840px; width: 110px; height: 165px; background: linear-gradient(#f4f4f1, #d9d9d5); border-radius: 6px; }

  .panel {
    position: absolute; left: 212px; top: 0; width: 524px; height: 1058px;
    background: var(--brand-red); color: var(--white); text-align: center;
  }
  .brand { position: absolute; left: 0; top: 20px; width: 524px; height: 120px; }
  .brand__mark { position: absolute; left: 26px; top: 18px; width: 78px; height: 78px; border-radius: 50%; background: var(--white); }
  .brand__name {
    position: absolute; left: 116px; top: 12px; text-align: left; white-space: nowrap;
    font-weight: 700; font-size: 57px; line-height: 60px;
  }
  .brand__name span { display: block; font-weight: 400; font-size: 44px; line-height: 52px; margin-left: 52px; }
  .tagline { position: absolute; left: 0; top: 260px; width: 524px; font-family: "Archivo Black", "Arial Black", sans-serif; font-size: 41px; }
  .services-title { position: absolute; left: 0; top: 332px; width: 524px; font-family: "Cabin", sans-serif; font-weight: 700; font-size: 64px; letter-spacing: 1px; }
  .services { position: absolute; left: 0; top: 430px; width: 524px; list-style: none; font-size: 36.5px; line-height: 52px; }
  .tick { width: 20px; height: 20px; margin-right: 8px; vertical-align: 1px; }
  .rec { position: absolute; left: 0; top: 972px; width: 524px; font-size: 35px; }

  .contact { position: absolute; left: 0; top: 1058px; width: 938px; height: 142px; text-align: center; color: var(--contact-red); }
  .contact__line { font-size: 33px; line-height: 40px; }
  .contact__line--first { margin-top: 34px; }
  .contact__line strong { font-size: 38px; font-weight: 700; }
  .contact__gap { display: inline-block; width: 36px; }
</style>
</head>
<body>
<main class="flyer">
  <div class="wall" role="img" aria-label="Red brick wall background"></div>
  <div class="fixture fixture--track" role="img" aria-label="Ceiling track lighting"></div>
  <div class="fixture fixture--flood" role="img" aria-label="Twin security floodlight"></div>
  <div class="fixture fixture--sconce" role="img" aria-label="Chrome wall sconce with glass shade"></div>
  <div class="fixture fixture--lamp" role="img" aria-label="Wall lamp with cream shade"></div>
  <div class="fixture fixture--lantern" role="img" aria-label="Bronze wall lantern"></div>
  <div class="fixture fixture--chandelier" role="img" aria-label="Crystal chandelier"></div>
  <div class="fixture fixture--fan" role="img" aria-label="Ceiling fan with light"></div>
  <div class="fixture fixture--board" role="img" aria-label="Electrical switchboard"></div>
  <div class="fixture fixture--outlet" role="img" aria-label="Wall power outlet"></div>

  <section class="panel">
    <div class="brand">
      <div class="brand__mark"></div>
      <h1 class="brand__name">DALE HURST<span>ELECTRICAL</span></h1>
    </div>
    <p class="tagline">NO JOB TOO SMALL</p>
    <h2 class="services-title">SERVICES</h2>
    <ul class="services">
      <li><svg class="tick" viewBox="0 0 18 18"><path d="M3 9l4 4 8-8" fill="none" stroke="#fff" stroke-width="3"/></svg>Extensions / Renovations</li>
      <li><svg class="tick" viewBox="0 0 18 18"><path d="M3 9l4 4 8-8" fill="none" stroke="#fff" stroke-width="3"/></svg>Safety Switch and<br>Switchboard Upgrades</li>
      <li><svg class="tick" viewBox="0 0 18 18"><path d="M3 9l4 4 8-8" fill="none" stroke="#fff" stroke-width="3"/></svg>LED Lighting including<br>downlights/light fittings and<br>LED strip light</li>
      <li><svg class="tick" viewBox="0 0 18 18"><path d="M3 9l4 4 8-8" fill="none" stroke="#fff" stroke-width="3"/></svg>Re-wires</li>
      <li><svg class="tick" viewBox="0 0 18 18"><path d="M3 9l4 4 8-8" fill="none" stroke="#fff" stroke-width="3"/></svg>Maintenance (mainly<br>domestic)</li>
    </ul>
    <p class="rec">REC - 38517</p>
  </section>

  <footer class="contact">
    <p class="contact__line contact__line--first">Phone - <strong>0437 216 580</strong><span class="contact__gap"></span>ABN - <strong>42 318 570 264</strong></p>
    <p class="contact__line">Email - hurstelectrical@sparkmailbox.net</p>
  </footer>
</main>
</body>
</html>
```